Social Media Graphics - Copperfield Loop

Create 6-7 individual social media graphics (square size) to encourage folks to join our online course, using either of the text below (only one set of text per graphic:

The Lantern Ridge Method
How to Create a 7-Figure Business From Scratch
Sign Up Today!

Or

The Lantern Ridge Method
Fast-track Your Way to a Multi-Million Business!
Sign Up Today!

For the color scheme of the graphics, use 1 or 2 colors in the color palette attached; or use any colors that look nice with their outfits; AVOID using red, white and blue altogether because it will look like an Independence Day (4th of July) graphic and we don’t want that; make sure the graphics appeal to both men and women

Make sure each graphic contains 1 of the 2 pics attached; and make sure one of the graphics is all TEXT only.

Target Market(s)

men and women looking to make more money

Industry/Entity Type

entrepreneurship

Requirements
Must have
• see the text document attached
Nice to have
• We are open to a nice color design; the color palette colors are not required, especially we don't want red, white and blue used together
Should not have
• AVOID using red, white and blue altogether because it will look like an Independence Day (4th of July) graphic and we dont want that

```html
<!DOCTYPE html>
<html lang="en">
<head>
<meta charset="UTF-8">
<title>The Lantern Ridge Method – Sign Up</title>
<link rel="stylesheet" href="https://fonts.googleapis.com/css2?family=Oswald:wght@500;700&family=Montserrat:wght@300&family=Poppins:wght@700&display=swap">
<style>
  :root {
    --brand-red: #c8102e;
    --brand-red-deep: #b00d27;
    --brand-red-bright: #e32238;
    --blush: #ffd3d8;
    --blush-text: #ffe3e6;
    --dress-pink: #e8335a;
    --jacket-dark: #2a2325;
    --paper: #ffffff;
  }
  * { margin: 0; padding: 0; box-sizing: border-box; }
  html, body { width: 1200px; height: 1199px; overflow: hidden; background: var(--paper); }
  .social-tile {
    position: relative;
    width: 1200px;
    height: 1199px;
    background: var(--paper);
    overflow: hidden;
  }
  .backdrop { position: absolute; inset: 0; }
  .accent-square {
    position: absolute;
    border-radius: 4px;
  }
  .accent-square--top {
    left: 60px; top: 55px; width: 82px; height: 112px;
    background: rgba(200, 16, 46, .14);
  }
  .accent-square--bottom {
    left: 1043px; top: 1035px; width: 82px; height: 82px;
    background: rgba(255, 138, 150, .22);
  }
  .title-lockup { position: absolute; left: 60px; top: 150px; }
  .title-lockup text { font-family: "Oswald", sans-serif; font-weight: 700; fill: var(--brand-red); }
  .hosts-photo {
    position: absolute;
    left: 477px; top: 90px;
    width: 723px; height: 693px;
    border-radius: 300px 300px 0 0;
    background:
      linear-gradient(180deg, rgba(255,211,216,1) 0%, rgba(255,211,216,0) 38%),
      linear-gradient(90deg, var(--dress-pink) 0%, #d42a4f 44%, #4a3236 56%, var(--jacket-dark) 100%);
  }
  .cta-band {
    position: absolute;
    left: 0; top: 783px;
    width: 1200px; height: 416px;
    background: var(--brand-red);
  }
  .cta-band__tagline {
    position: absolute;
    left: 0; top: 62px; width: 100%;
    text-align: center;
    font-family: "Montserrat", sans-serif;
    font-weight: 300;
    font-size: 64px;
    line-height: 68px;
    letter-spacing: 1px;
    color: var(--blush-text);
    text-transform: uppercase;
  }
  .cta-button {
    position: absolute;
    left: 316px; top: 249px;
    width: 567px; height: 89px;
    border-radius: 45px;
    background: linear-gradient(90deg, var(--brand-red-deep), var(--brand-red-bright) 50%, var(--brand-red-deep));
    box-shadow: 0 10px 18px rgba(90, 0, 15, .45);
    display: flex; align-items: center; justify-content: center;
    font-family: "Poppins", sans-serif;
    font-weight: 700;
    font-size: 54px;
    color: var(--blush-text);
    text-transform: uppercase;
  }
</style>
</head>
<body>
<main class="social-tile">
  <svg class="backdrop" width="1200" height="1199" viewBox="0 0 1200 1199" aria-hidden="true">
    <polygon points="727,0 1110,0 1200,289 1200,783 477,783" fill="var(--blush)"/>
  </svg>

  <div class="accent-square accent-square--top" role="img" aria-label="Small decorative dot grid"></div>

  <svg class="title-lockup" width="400" height="570" viewBox="0 0 400 570" role="heading" aria-level="1" aria-label="The Lantern Ridge Method">
    <defs>
      <linearGradient id="title-fill" x1="0" y1="0" x2="1" y2="1">
        <stop offset="0" stop-color="#e32238"/>
        <stop offset="1" stop-color="#a80b24"/>
      </linearGradient>
    </defs>
    <text x="143" y="72" font-size="88" textLength="117" lengthAdjust="spacingAndGlyphs">THE</text>
    <text x="12" y="228" font-size="150" textLength="384" lengthAdjust="spacingAndGlyphs" style="fill:url(#title-fill)">LANTERN</text>
    <text x="12" y="430" font-size="200" textLength="384" lengthAdjust="spacingAndGlyphs" style="fill:url(#title-fill)">RIDGE</text>
    <text x="12" y="552" font-size="100" textLength="384" lengthAdjust="spacingAndGlyphs">METHOD</text>
  </svg>

  <div class="hosts-photo" role="img" aria-label="Photo of the two course hosts smiling, a woman in a pink dress with arms crossed and a man in a black shirt and jacket"></div>

  <section class="cta-band">
    <p class="cta-band__tagline">Fast-track your way to a<br>multi-million business!</p>
    <div class="cta-button">Sign up today!</div>
  </section>

  <div class="accent-square accent-square--bottom" role="img" aria-label="Small decorative dot grid"></div>
</main>
</body>
</html>
```